**URGENT // ENVIRONMENTAL // QUICK TURN AROUND**

We are looking for an A-Grade designer to work with longterm, starting with the successful design for our website & logo; Kestrel Hub.

Kestrel Hub is a business that focusses on grouping environmentally conscious people together and helping them get "bulk buy" discounts by purchasing large volumes together; solar, energy efficency, wind turbines, and the like.

The Logo and website must have a green feel, as we are here to protect the environment, whilst also helping our customers save money.

The website must also have a blog feature, allowing us to post and keep people up to date with the latest in the industry.

Target Market(s)

FAMILIES WITHIN REGIONAL AUSTRALIA WANTING TO EITHER SAVE MONEY ON ELECTRICITY BILLS, OR REDUCE CARBON EMISSIONS.

Industry/Entity Type

Solar Energy

Logo Text

KESTREL HUB

Number of Pages Required

5+ page

Font styles to use
Serif
Sans Serif

Colors

Designer to choose colors to be used in the design.

Requirements
Must have
• 1.HOME PAGE
• 2.OUR SERVICES PAGE
• - RENEWABLE ENERGY
• - LIGHTING SYSTEMS
• - ENERGY ASSESSMENT
• - R.H.L.P SCHEME
• - ENERGY COMPARISON
• 4. BOOK AN APPOINTMENT
• 5. IN THE NEWS
• 6. SUBSCRIBE TO NEWSLETTER
• 7. CONTACT US
• MUST LOOK VERY PROFESSIONAL, WITH LOTS OF INFORMATION, IT CANNOT BE BARE AND SIMPLE.
• Can use www.tarnfieldgoodsandwares.com.au which is our other brand for copy and ideas - HOWEVER, THIS IS THE REASON WE ARE RE-BRANDING, AS THIS BRAND HAS COME UNDER FAR TOO MUCH CRITICISM FOR LACK OF INFORMATION AND LOOKING TO SIMPLE.
Nice to have
• BLOG FEATURE
Should not have
• ANYTHING THAT APPEARS NON-ENVIRONMENTALS

```html
<!DOCTYPE html>
<html lang="en">
<head>
<meta charset="utf-8">
<title>Kestrel Hub — Home</title>
<link rel="stylesheet" href="https://fonts.googleapis.com/css2?family=Merriweather:wght@400;700&family=Lato:wght@400;700&display=swap">
<style>
:root{
  --backdrop:#ececec;
  --page:#ffffff;
  --green:#3f9a36;
  --green-bright:#5ab52e;
  --green-lime:#b5d334;
  --green-dark:#136a2b;
  --green-deeper:#0f5c24;
  --ink:#2b2b2b;
  --text:#555a55;
  --muted:#9a9a9a;
  --line:#c9c9c9;
  --footer-text:#e6f2e6;
  --footer-link:#7fe36a;
  --serif:'Merriweather', Georgia, serif;
  --sans:'Lato', Arial, sans-serif;
}
*{margin:0;padding:0;box-sizing:border-box}
html,body{width:1000px;height:1200px;overflow:hidden;background:var(--backdrop)}
body{position:relative;font-family:var(--sans);color:var(--text)}
a{text-decoration:none}
.page{position:absolute;left:179px;top:0;width:666px;height:1165px;background:var(--page);box-shadow:0 0 40px rgba(0,0,0,.18);overflow:hidden}
.abs{position:absolute}

/* top strip */
.strip-photo{left:0;top:0;width:404px;height:15px;background:linear-gradient(90deg,#7d8f86,#5e8a4a 60%,#4b8a35)}
.strip-band{left:404px;top:0;width:262px;height:15px;background:var(--green)}

/* intro */
.intro-title{left:0;width:666px;top:52px;text-align:center;font-family:var(--serif);font-weight:400;font-size:24px;color:var(--green)}
.intro-text{left:88px;width:490px;top:88px;text-align:center;font-size:8.2px;line-height:15px;color:var(--text)}

/* blog cards */
.card{top:156px;width:190px}
.card-photo{width:190px;height:142px}
.card-date{margin-top:10px;font-size:6.3px;color:var(--muted)}
.card-title{margin-top:2px;font-family:var(--serif);font-size:11px;line-height:13px;color:var(--ink);font-weight:400}
.photo-forest{background:linear-gradient(180deg,#6fa5b8 0%,#2f5a3b 40%,#1e3d24 100%)}
.photo-wheat{background:linear-gradient(180deg,#c8da7a 0%,#8fb046 55%,#5c8a2e 100%)}
.photo-cedar{background:radial-gradient(circle at 60% 60%,#a7d24a,#6b9e1c 55%,#3e6b12)}

.blog-note{left:190px;width:286px;top:377px;text-align:center;font-size:6.3px;line-height:11px;color:var(--muted)}
.blog-note a{color:var(--green-bright)}
.btn-blog{left:188px;top:417px;width:298px;height:23px;background:var(--green-bright);color:#fff;font-size:8px;display:flex;align-items:center;justify-content:center}

/* mission */
.scenery{left:0;top:560px;width:666px;height:382px;background:linear-gradient(180deg,#ffffff 0%,#f3f3f3 25%,#eaeaea 55%,#d4d4d4 75%,#b4b4b4 100%)}
.mission-title{left:35px;top:480px;font-family:var(--serif);font-size:11.5px;color:var(--ink);font-weight:400}
.mission-lead{left:35px;top:502px;width:290px;font-size:8px;line-height:14px;color:var(--text)}
.mission-body{left:35px;top:538px;width:295px;font-size:6.8px;line-height:11px;color:var(--text)}
.pledge-art{left:457px;top:480px;width:64px;height:62px;border-radius:50%;background:radial-gradient(circle,#d9efc7 0%,#eef8e6 60%,rgba(255,255,255,0) 72%)}
.pledge-caption{left:380px;width:220px;top:554px;text-align:center;font-size:7.8px;color:var(--text)}

.frame{left:61px;top:603px;width:254px;height:186px;border:2px solid var(--green);border-top-color:var(--green-lime);border-right-color:var(--green-lime)}
.photo-windmill{left:83px;top:623px;width:251px;height:179px;background:linear-gradient(180deg,#7aa3d9 0%,#b9cde6 45%,#e9d84a 52%,#f0d91c 100%)}
.frame-label{left:-20px;top:720px;width:130px;transform:rotate(-90deg);transform-origin:center;text-align:center;font-family:var(--serif);font-weight:700;font-size:10px;color:var(--green-lime);letter-spacing:.3px}

.rating-label{left:360px;width:260px;text-align:center;font-size:7.5px;color:var(--muted)}
.rating{left:382px;display:flex;gap:4.5px}
.rating span{width:18px;height:18px;border:1px solid var(--line);border-radius:50%;display:flex;align-items:center;justify-content:center;background:#fff}

/* footer */
.footer{left:0;top:942px;width:666px;height:223px;background:var(--green-dark);color:var(--footer-text)}
.footer .col{position:absolute;top:38px;width:140px;font-size:7px;line-height:10px}
.brand{font-family:var(--serif);font-size:12px;color:#fff;display:flex;align-items:center;gap:5px;letter-spacing:.5px}
.brand i{width:10px;height:10px;border:1.5px solid #fff;border-radius:50%;display:block}
.col-title{font-family:var(--serif);font-size:11.5px;color:#fff;margin-bottom:8px;font-weight:400}
.social{display:flex;gap:8px;margin:12px 0 9px}
.social span{width:14px;height:14px;border-radius:50%;background:var(--green-bright)}
.footer a{color:var(--footer-link)}
.post{display:flex;background:var(--green-deeper);margin-bottom:4px;height:41px}
.post-body{flex:1;padding:4px 6px;font-size:7px;line-height:9px;color:#fff}
.post-date{margin-top:5px;color:#9ec79e;font-size:6.6px}
.post-thumb{width:41px;height:41px}
.program{display:flex;align-items:center;gap:5px;margin-top:4px;color:var(--footer-link)}
.program svg{flex:none}
.footer p+p{margin-top:6px}
.footer-rule{left:0;top:181px;width:666px;height:1px;background:rgba(255,255,255,.08)}
.copyright{left:38px;top:198px;font-size:7.2px;color:#fff}
.to-top{left:620px;top:198px}
</style>
</head>
<body>
<main class="page">
  <div class="abs strip-photo" role="img" aria-label="Landscape photo strip"></div>
  <div class="abs strip-band"></div>

  <h1 class="abs intro-title">Fusce rutrum volutpat faucibus</h1>
  <p class="abs intro-text">Onceptos himenaeos. Mauris in erat justo. Nullam ac urna eu felis dapibus condimentum sit amet a augue. Sed non neque elit. Sed ut imperdiet nisi. Proin condimentum fermentum nunc. Etiam pharetra, erat sed fermentum feugiat, velit mauris egestas quam, ut aliquam massa nisl quis neque. Suspendisse in orci enim.</p>

  <article class="abs card" style="left:43px">
    <div class="card-photo photo-forest" role="img" aria-label="Conifer forest under a blue sky"></div>
    <div class="card-date">May 8, 2017</div>
    <h2 class="card-title">Vestibulum commodo volutpat laoreet</h2>
  </article>
  <article class="abs card" style="left:242px">
    <div class="card-photo photo-wheat" role="img" aria-label="Close-up of green wheat ears"></div>
    <div class="card-date">May 7, 2017</div>
    <h2 class="card-title">Quisque lorem tortor fringilla bulum</h2>
  </article>
  <article class="abs card" style="left:442px">
    <div class="card-photo photo-cedar" role="img" aria-label="Close-up of a green cedar branch"></div>
    <div class="card-date">May 6, 2017</div>
    <h2 class="card-title">Vivamus sit amet metus sem imperdiet</h2>
  </article>

  <p class="abs blog-note">Fusce ac porttitor elit. In <a href="#">sed feugiat turpis</a>, dictum semper ante. Phasellus luctus, sapien sit amet ullamcorper ultrices, tortor odio hendrerit ante, ut amet.</p>
  <a class="abs btn-blog" href="#">Read our blog</a>

  <div class="abs scenery" role="img" aria-label="Misty sky fading into a grey mountain range"></div>

  <h2 class="abs mission-title">Vestibulum ornare convallis</h2>
  <p class="abs mission-lead">Lorem ipsum dolor sit amet, consectetur adipiscing elit. Curabitur et semper libero, quis tristique nisl. Vivamus eget posuere ligula.</p>
  <p class="abs mission-body">Duis et nunc ullamcorper, semper nisl at, tristique neque. Curabitur at rhoncus velit. Etiam pharetra auctor dapibus. Quisque et augue tortor. Pellentesque sed. Sed viverra, felis ut aliquam sagittis, tortor nunc cursus massa, quis tristique ipsum diam ut mi.</p>

  <div class="abs pledge-art" role="img" aria-label="Illustration of a hand holding the globe"></div>
  <p class="abs pledge-caption">Duis convallis purus a convallis ornare</p>

  <div class="abs frame"></div>
  <div class="abs photo-windmill" role="img" aria-label="Traditional windmill behind a yellow rapeseed field"></div>
  <div class="abs frame-label">Traditional windmill</div>

  <p class="abs rating-label" style="top:605px">Nam pharetra urna non interdum feugiat</p>
  <div class="abs rating" style="top:624px">
    <span><svg width="10" height="10" viewBox="0 0 10 10" fill="none" stroke="#aaa" stroke-width=".8"><circle cx="5" cy="5" r="2"/><path d="M5 0v1.5M5 8.5V10M0 5h1.5M8.5 5H10M1.5 1.5l1 1M7.5 7.5l1 1M1.5 8.5l1-1M7.5 2.5l1-1"/></svg></span>
    <span><svg width="10" height="10" viewBox="0 0 10 10" fill="none" stroke="#aaa" stroke-width=".8"><circle cx="5" cy="5" r="2"/><path d="M5 0v1.5M5 8.5V10M0 5h1.5M8.5 5H10M1.5 1.5l1 1M7.5 7.5l1 1M1.5 8.5l1-1M7.5 2.5l1-1"/></svg></span>
    <span><svg width="10" height="10" viewBox="0 0 10 10" fill="none" stroke="#aaa" stroke-width=".8"><circle cx="5" cy="5" r="2"/><path d="M5 0v1.5M5 8.5V10M0 5h1.5M8.5 5H10M1.5 1.5l1 1M7.5 7.5l1 1M1.5 8.5l1-1M7.5 2.5l1-1"/></svg></span>
    <span><svg width="10" height="10" viewBox="0 0 10 10" fill="none" stroke="#aaa" stroke-width=".8"><circle cx="5" cy="5" r="2"/><path d="M5 0v1.5M5 8.5V10M0 5h1.5M8.5 5H10M1.5 1.5l1 1M7.5 7.5l1 1M1.5 8.5l1-1M7.5 2.5l1-1"/></svg></span>
    <span><svg width="10" height="10" viewBox="0 0 10 10" fill="none" stroke="#aaa" stroke-width=".8"><circle cx="5" cy="5" r="2"/><path d="M5 0v1.5M5 8.5V10M0 5h1.5M8.5 5H10M1.5 1.5l1 1M7.5 7.5l1 1M1.5 8.5l1-1M7.5 2.5l1-1"/></svg></span>
    <span><svg width="10" height="10" viewBox="0 0 10 10" fill="none" stroke="#aaa" stroke-width=".8"><circle cx="5" cy="5" r="2"/><path d="M5 0v1.5M5 8.5V10M0 5h1.5M8.5 5H10M1.5 1.5l1 1M7.5 7.5l1 1M1.5 8.5l1-1M7.5 2.5l1-1"/></svg></span>
    <span><svg width="10" height="10" viewBox="0 0 10 10" fill="none" stroke="#aaa" stroke-width=".8"><circle cx="5" cy="5" r="2"/><path d="M5 0v1.5M5 8.5V10M0 5h1.5M8.5 5H10M1.5 1.5l1 1M7.5 7.5l1 1M1.5 8.5l1-1M7.5 2.5l1-1"/></svg></span>
    <span><svg width="10" height="10" viewBox="0 0 10 10" fill="none" stroke="#aaa" stroke-width=".8"><circle cx="5" cy="5" r="2"/><path d="M5 0v1.5M5 8.5V10M0 5h1.5M8.5 5H10M1.5 1.5l1 1M7.5 7.5l1 1M1.5 8.5l1-1M7.5 2.5l1-1"/></svg></span>
    <span><svg width="10" height="10" viewBox="0 0 10 10" fill="none" stroke="#aaa" stroke-width=".8"><circle cx="5" cy="5" r="2"/><path d="M5 0v1.5M5 8.5V10M0 5h1.5M8.5 5H10M1.5 1.5l1 1M7.5 7.5l1 1M1.5 8.5l1-1M7.5 2.5l1-1"/></svg></span>
    <span><svg width="10" height="10" viewBox="0 0 10 10" fill="none" stroke="#aaa" stroke-width=".8"><circle cx="5" cy="5" r="2"/><path d="M5 0v1.5M5 8.5V10M0 5h1.5M8.5 5H10M1.5 1.5l1 1M7.5 7.5l1 1M1.5 8.5l1-1M7.5 2.5l1-1"/></svg></span>
  </div>

  <p class="abs rating-label" style="top:655px">Etiam eget velit non mi auctor semper sit amet</p>
  <div class="abs rating" style="top:674px">
    <span><svg width="10" height="10" viewBox="0 0 10 10" fill="none" stroke="#aaa" stroke-width=".8"><path d="M1 9C2 4 5 1 9 1 9 6 6 8 1 9zM1 9l5-5"/></svg></span>
    <span><svg width="10" height="10" viewBox="0 0 10 10" fill="none" stroke="#aaa" stroke-width=".8"><path d="M1 9C2 4 5 1 9 1 9 6 6 8 1 9zM1 9l5-5"/></svg></span>
    <span><svg width="10" height="10" viewBox="0 0 10 10" fill="none" stroke="#aaa" stroke-width=".8"><path d="M1 9C2 4 5 1 9 1 9 6 6 8 1 9zM1 9l5-5"/></svg></span>
    <span><svg width="10" height="10" viewBox="0 0 10 10" fill="none" stroke="#aaa" stroke-width=".8"><path d="M1 9C2 4 5 1 9 1 9 6 6 8 1 9zM1 9l5-5"/></svg></span>
    <span><svg width="10" height="10" viewBox="0 0 10 10" fill="none" stroke="#aaa" stroke-width=".8"><path d="M1 9C2 4 5 1 9 1 9 6 6 8 1 9zM1 9l5-5"/></svg></span>
    <span><svg width="10" height="10" viewBox="0 0 10 10" fill="none" stroke="#aaa" stroke-width=".8"><path d="M1 9C2 4 5 1 9 1 9 6 6 8 1 9zM1 9l5-5"/></svg></span>
    <span><svg width="10" height="10" viewBox="0 0 10 10" fill="none" stroke="#aaa" stroke-width=".8"><path d="M1 9C2 4 5 1 9 1 9 6 6 8 1 9zM1 9l5-5"/></svg></span>
    <span><svg width="10" height="10" viewBox="0 0 10 10" fill="none" stroke="#aaa" stroke-width=".8"><path d="M1 9C2 4 5 1 9 1 9 6 6 8 1 9zM1 9l5-5"/></svg></span>
    <span><svg width="10" height="10" viewBox="0 0 10 10" fill="none" stroke="#aaa" stroke-width=".8"><path d="M1 9C2 4 5 1 9 1 9 6 6 8 1 9zM1 9l5-5"/></svg></span>
    <span><svg width="10" height="10" viewBox="0 0 10 10" fill="none" stroke="#aaa" stroke-width=".8"><path d="M1 9C2 4 5 1 9 1 9 6 6 8 1 9zM1 9l5-5"/></svg></span>
  </div>

  <footer class="abs footer">
    <div class="col" style="left:38px">
      <div class="brand">KESTREL HUB <i></i></div>
      <p style="margin-top:12px;color:#fff">Duis dictum eleifend tortor at scelerisque. Sed elementum augue eu.</p>
      <div class="social"><span></span><span></span><span></span><span></span><span></span></div>
      <p style="color:#fff">Contact us: +61 (0) 3 5550 1427<br>Write us: &nbsp;<a href="#">hello@kestrelhub.com.au</a></p>
    </div>

    <div class="col" style="left:191px">
      <h3 class="col-title">Recent posts</h3>
      <div class="post">
        <div class="post-body">Vestibulum commodo volutpat laoreet<div class="post-date">◷ &nbsp;May 8, 2017</div></div>
        <div class="post-thumb photo-forest" role="img" aria-label="Forest thumbnail"></div>
      </div>
      <div class="post">
        <div class="post-body">Quisque lorem tortor fringilla bulum<div class="post-date">◷ &nbsp;May 7, 2017</div></div>
        <div class="post-thumb photo-wheat" role="img" aria-label="Wheat thumbnail"></div>
      </div>
    </div>

    <div class="col" style="left:343px">
      <h3 class="col-title">Programs</h3>
      <p style="color:#fff;margin-bottom:6px">Vitae adipiscing turpis. Aenean ligula nibh in, molestie id viverra a, dapibus at dolor elit lectus felis.</p>
      <div class="program"><svg width="8" height="8" viewBox="0 0 8 8" fill="none" stroke="#fff" stroke-width=".9"><circle cx="4" cy="4" r="3.4"/><path d="M2.4 4l1.1 1.1L5.6 3"/></svg>Mauris in erat justo venenatis</div>
      <div class="program"><svg width="8" height="8" viewBox="0 0 8 8" fill="none" stroke="#fff" stroke-width=".9"><circle cx="4" cy="4" r="3.4"/><path d="M2.4 4l1.1 1.1L5.6 3"/></svg>Interdum nulla lectus vel</div>
      <div class="program"><svg width="8" height="8" viewBox="0 0 8 8" fill="none" stroke="#fff" stroke-width=".9"><circle cx="4" cy="4" r="3.4"/><path d="M2.4 4l1.1 1.1L5.6 3"/></svg>Ut enim ad minim veniam</div>
    </div>

    <div class="col" style="left:496px">
      <h3 class="col-title">The company</h3>
      <p style="color:#fff">Nulla risus ante, luctus et placerat quis, efficitur nec nisl. Cras iaculis tristique.</p>
      <p style="color:#fff">Etiam at nibh turpis! Vestibulum mattis risus eget dolor finibus, ut luctus est congue. Ut sit amet interdum erat; quis malesuada lacus. Sed mauris diam, sodales a imperdiet ut.</p>
    </div>

    <div class="abs footer-rule"></div>
    <p class="abs copyright">© 2017 &nbsp;All Rights Reserved.</p>
    <svg class="abs to-top" width="10" height="8" viewBox="0 0 10 8" fill="none" stroke="#3f9a36" stroke-width="1"><path d="M2 5l3-3 3 3"/></svg>
  </footer>
</main>
</body>
</html>
```